Stationery design for a Saas platform at PR industry

Hello, Corvanta is a media database and press release distribution platform targeting Public Relations agencies and corporates. We started at Turkey and moved our HQ to San Francisco, US. We changed our website and need a new stationary design with compatible of the hew website. Our website address is http://www.corvanta-example.com/en
Updates
Reason: The number of the designers are not enough for us. Looking for some other good designs.
Industry/Entity Type
Industry
Requirements
Must have
- Statinery covers business card design, letterhead, envalope, file and invoice design.

```html
<!DOCTYPE html>
<html lang="en">
<head>
<meta charset="utf-8">
<title>Corvanta Letterhead</title>
<link href="https://fonts.googleapis.com/css2?family=Open+Sans:wght@400;600;700&display=swap" rel="stylesheet">
<style>
  :root {
    --backdrop: #8fc3e2;
    --paper: #ffffff;
    --brand-blue: #2a6fb0;
    --brand-teal: #6cc9c4;
    --rule-grey: #8a8f96;
    --ink: #1b1e22;
    --muted: #7a7f86;
    --band-start: #bfe9e4;
    --band-end: #5fc2bd;
  }
  * { box-sizing: border-box; margin: 0; padding: 0; }
  html, body { width: 1200px; height: 784px; overflow: hidden; }
  body {
    background: var(--backdrop);
    font-family: "Open Sans", Arial, sans-serif;
    display: flex; align-items: center; justify-content: center;
  }
  .letterhead {
    position: relative;
    width: 524px; height: 740px;
    background: var(--paper);
    box-shadow: 0 6px 18px rgba(30, 80, 120, .25);
    overflow: hidden;
  }
  .letterhead__header {
    position: absolute; top: 18px; left: 0; right: 0;
    display: flex; align-items: center; height: 30px;
  }
  .rule { height: 3px; }
  .rule--blue { background: var(--brand-blue); }
  .rule--teal { background: var(--brand-teal); }
  .rule--grey { background: var(--rule-grey); }
  .letterhead__header .rule--blue { width: 150px; }
  .letterhead__header .rule--teal { flex: 1; }
  .brand {
    display: flex; align-items: center; gap: 6px;
    padding: 0 8px;
  }
  .brand__dot {
    width: 18px; height: 18px; border-radius: 50%;
    background: var(--brand-blue);
  }
  .brand__name {
    font-weight: 700; font-size: 26px; letter-spacing: .3px;
    color: var(--ink); line-height: 1;
  }
  .letterhead__footer {
    position: absolute; left: 0; right: 0; bottom: 0; height: 56px;
  }
  .contact {
    position: absolute; left: 12px; bottom: 32px;
    display: flex; gap: 10px; align-items: center;
    font-size: 7.5px; color: var(--muted); white-space: nowrap;
    line-height: 1;
  }
  .contact__item { display: flex; align-items: center; gap: 3px; }
  .contact__icon { width: 8px; height: 8px; flex: none; }
  .footer-rules {
    position: absolute; left: 0; bottom: 24px; width: 330px;
    display: flex;
  }
  .footer-rules .rule--blue { width: 90px; }
  .footer-rules .rule--grey { width: 110px; }
  .footer-rules .rule--teal { flex: 1; }
  .web-band {
    position: absolute; right: 0; bottom: 0;
    width: 194px; height: 27px;
    background: linear-gradient(90deg, var(--band-start), var(--band-end));
    display: flex; align-items: center; justify-content: center;
    font-weight: 700; font-size: 11px; line-height: 1;
    color: var(--ink); white-space: nowrap;
  }
  .web-band::before {
    content: ""; position: absolute; left: -14px; top: 0;
    border-right: 14px solid var(--band-start);
    border-top: 27px solid transparent;
  }
</style>
</head>
<body>
  <main class="letterhead">
    <header class="letterhead__header">
      <div class="rule rule--blue"></div>
      <div class="brand">
        <span class="brand__dot"></span>
        <span class="brand__name">Corvanta</span>
      </div>
      <div class="rule rule--teal"></div>
    </header>

    <footer class="letterhead__footer">
      <div class="contact">
        <span class="contact__item">
          <svg class="contact__icon" viewBox="0 0 10 10"><circle cx="5" cy="5" r="5" fill="#2a6fb0"/><path d="M5 2.2a1.8 1.8 0 0 0-1.8 1.8C3.2 5.4 5 7.8 5 7.8S6.8 5.4 6.8 4A1.8 1.8 0 0 0 5 2.2z" fill="#fff"/></svg>
          0000 Harbor View example Brookline, Oregon 0000
        </span>
        <span class="contact__item">
          <svg class="contact__icon" viewBox="0 0 10 10"><circle cx="5" cy="5" r="5" fill="#2a6fb0"/><path d="M3.2 2.6l1 1-.6.7c.4.8 1 1.4 1.8 1.8l.7-.6 1 1-.7.8C4.8 7.1 2.9 5.2 2.6 3.3z" fill="#fff"/></svg>
          (000) 000-4821
        </span>
        <span class="contact__item">
          <svg class="contact__icon" viewBox="0 0 10 10"><circle cx="5" cy="5" r="5" fill="#2a6fb0"/><rect x="2.6" y="3.3" width="4.8" height="3.4" fill="#fff"/><path d="M2.6 3.3L5 5.2l2.4-1.9" fill="none" stroke="#2a6fb0" stroke-width=".5"/></svg>
          info@corvanta-example.com
        </span>
      </div>
      <div class="footer-rules">
        <div class="rule rule--blue"></div>
        <div class="rule rule--grey"></div>
        <div class="rule rule--teal"></div>
      </div>
      <div class="web-band">www.corvanta-example.com/en</div>
    </footer>
  </main>
</body>
</html>
```